Business Card Design

We would like a business card that utilizes our current logo and keeps with the same feel - elegant and organic. Our farm isn't about mass production, it's about excellence, education, beautiful events and flowers - people, culture, and community.

Target Market(s)

Patrons to our farm who are interested in weddings, events, or our flowers and vegetables.

Contact Information for Business Card

Name, address, cell email (Danielle Hoskins, 2716 Wrenfield Rd, Alder Bend, OR 97411, cell 30.412.6638, email danielle@wrenfieldacres.com)

```html
<!DOCTYPE html>
<html lang="en">
<head>
<meta charset="UTF-8">
<title>Wrenfield Acres Business Card</title>
<link rel="stylesheet" href="https://fonts.googleapis.com/css2?family=Cormorant+Garamond:wght@500&family=Poppins:wght@400&display=swap">
<style>
  :root {
    --backdrop: #999999;
    --paper: #f7f7f5;
    --sage: #6f8a6e;
    --band: #667c64;
    --ink: #4d5a4e;
    --white: #ffffff;
  }
  * { margin: 0; padding: 0; box-sizing: border-box; }
  html, body {
    width: 1200px;
    height: 1200px;
    overflow: hidden;
    background: var(--backdrop);
  }
  .card {
    position: absolute;
    left: 180px;
    width: 840px;
    height: 480px;
    background: var(--paper);
    overflow: hidden;
  }
  .card--front { top: 99px; }
  .card--back { top: 620px; }

  .brand {
    position: absolute;
    left: 0;
    right: 0;
    text-align: center;
    font-family: "Poppins", sans-serif;
    font-weight: 400;
    color: var(--sage);
    font-size: 58px;
    letter-spacing: 1px;
    line-height: 1;
  }
  .card--front .brand { top: 200px; }
  .card--back .brand { top: 108px; }

  .front-address {
    position: absolute;
    top: 410px;
    left: 0;
    right: 0;
    text-align: center;
    font-family: "Poppins", sans-serif;
    font-size: 21px;
    letter-spacing: 5.2px;
    color: var(--ink);
  }

  .contact-band {
    position: absolute;
    left: 0;
    right: 0;
    top: 252px;
    bottom: 0;
    background: var(--band);
    color: var(--white);
    text-align: center;
  }
  .contact-name {
    margin-top: 24px;
    font-family: "Cormorant Garamond", serif;
    font-weight: 500;
    font-size: 50px;
    line-height: 1.1;
    letter-spacing: 0.5px;
    text-transform: uppercase;
  }
  .contact-line {
    font-family: "Poppins", sans-serif;
    font-size: 22px;
    line-height: 1;
    margin-top: 17px;
  }
  .contact-line:first-of-type { margin-top: 12px; }
</style>
</head>
<body>
  <section class="card card--front">
    <div class="brand">Wrenfield Acres</div>
    <p class="front-address">2716 Wrenfield Rd, Alder Bend, OR 97411</p>
  </section>

  <section class="card card--back">
    <div class="brand">Wrenfield Acres</div>
    <div class="contact-band">
      <h1 class="contact-name">Danielle Hoskins</h1>
      <p class="contact-line">30.412.6638</p>
      <p class="contact-line">danielle@wrenfieldacres.com</p>
      <p class="contact-line">2716 Wrenfield Rd, Alder Bend, OR 97411</p>
    </div>
  </section>
</body>
</html>
```